Business Card Design

I am a new realtor. To stand out from the other 25 realtors in my firm I need a card that will stand out. I am the youngest realtor here, so I want something to reflect that. Something different, as opposed to the same old traditional, boring cards everyone else has. It of course needs to have my picture which I will download for you ( I included a black and white option as well as color. Either are fine) and you can crop it or do whatever you need to make it look the best. Our company colors are red and white. These don't have to be the only colors on the card, but the red especially needs to be a focal color. I like a clean, stream-line look while still eye-catching. Not over the top busy.
While I do have to provide the company logo, I am a contractor. Therefore, I want the focus on me and my information.
Industry/Entity Type
Realtor
Contact Information for Business Card
Marisa Quillon
Realtor (this needs the realtor logo which has the R in the circle at the end)
(office)555.318.4406
(cell) 555.892.6035
Mquillon@brv-homegroup.example
It will also need our company logo which I will download and send
Requirements
Nice to have
- I like the look of the foil or metallic. However, this is definitely not a requirement

```html
<!DOCTYPE html>
<html lang="en">
<head>
<meta charset="utf-8">
<title>Marisa Quillon – Business Card</title>
<link href="https://fonts.googleapis.com/css2?family=Source+Sans+3:wght@400;600&display=swap" rel="stylesheet">
<style>
  :root {
    --brand-red: #d92026;
    --paper: #ffffff;
    --ink-light: #ffffff;
    --label-grey: #b5b5b5;
    --photo-light: #e9e9e9;
    --photo-dark: #6f6f6f;
    --card-shadow: 0 4px 10px rgba(0, 0, 0, 0.35);
  }
  * { box-sizing: border-box; margin: 0; padding: 0; }
  html, body {
    width: 1200px;
    height: 1000px;
    overflow: hidden;
    background: var(--paper);
    font-family: "Source Sans 3", "Helvetica Neue", Arial, sans-serif;
  }
  .sheet { position: relative; width: 1200px; height: 1000px; }

  .card {
    position: absolute;
    background: var(--brand-red);
    box-shadow: var(--card-shadow);
    overflow: hidden;
  }
  .card--front { left: 47px; top: 45px; width: 742px; height: 429px; }
  .card--back { left: 409px; top: 516px; width: 743px; height: 431px; }

  .side-label {
    position: absolute;
    font-size: 30px;
    font-weight: 400;
    letter-spacing: 4px;
    color: var(--label-grey);
  }
  .side-label--front { left: 138px; top: 496px; }
  .side-label--back { left: 970px; top: 460px; }

  .portrait {
    position: absolute;
    left: 0; top: 0;
    width: 307px; height: 429px;
    background: linear-gradient(180deg, var(--photo-light) 0%, #b9b9b9 45%, var(--photo-dark) 100%);
  }

  .contact {
    position: absolute;
    left: 374px;
    top: 118px;
    color: var(--ink-light);
    font-size: 23px;
    line-height: 1;
  }
  .contact__name { font-weight: 600; margin-bottom: 34px; }
  .contact__line { font-weight: 400; margin-bottom: 35px; }
  .contact__line:last-child { margin-bottom: 0; }

  .company {
    position: absolute;
    inset: 0;
    display: flex;
    flex-direction: column;
    align-items: center;
    justify-content: center;
    color: var(--ink-light);
    font-weight: 400;
    text-align: center;
  }
  .company__name { font-size: 60px; line-height: 1.55; letter-spacing: 1px; }
  .company__tagline { font-size: 46px; line-height: 1.6; }
</style>
</head>
<body>
<main class="sheet">
  <section class="card card--front" aria-label="Card front">
    <div class="portrait" role="img" aria-label="Black and white portrait photo of the realtor"></div>
    <div class="contact">
      <p class="contact__name">Marisa Quillon</p>
      <p class="contact__line">Realtor®</p>
      <p class="contact__line">555.318.4406 office</p>
      <p class="contact__line">555.892.6035 cell</p>
      <p class="contact__line">Mquillon@brv-homegroup.example</p>
    </div>
  </section>
  <p class="side-label side-label--front">FRONT</p>

  <p class="side-label side-label--back">BACK</p>
  <section class="card card--back" aria-label="Card back">
    <div class="company">
      <p class="company__name">HALDEN REYES<br>&amp; COMPANY</p>
      <p class="company__tagline">Real Estate Brokerage</p>
    </div>
  </section>
</main>
</body>
</html>
```